Website for Prestigious Trailers and Floats

Design a prestigious website, to be used on mobile phones, and computers.
Must be able to be edited by myself
Please refer to www.marrowbeckhaulage.com.au
Needs to focus on the "Marrowbeck Trailers"" name, and the "Dunmere Ashby Trailers" name.
Three trailer types to be highlighted are QX408/QX412 Horse Floats, RV3072 /RV81 Trailers, and LP5840/5296 Tipper Trailers
Needs Home Page,
Home page to include highlighted trailer types, slider for testimonials, Phone number, location, social media links, blog/news spot
Page for each of the highlighted trailer types/variations on the model
Page for multiple other trailer types

Logo's attached, can be broken up and used in parts if necessary for design

Target Market(s)

Western Australia, Horse People, Commercial Trailer Users, Handymen, Mini Digger Users, Tradesmen

Industry/Entity Type

Mining, Commercial, Government, Trades, Industry, Hobbyist

Coding

Coded - Design and coding required

Number of Pages Required

5+ page

Requirements
Must have
• See brief above
Nice to have
• See brief above

```html
<!DOCTYPE html>
<html lang="en">
<head>
<meta charset="utf-8">
<title>Marrowbeck Trailers – Home</title>
<link rel="stylesheet" href="https://fonts.googleapis.com/css2?family=Barlow:ital,wght@0,400;0,500;0,600;1,400&display=swap">
<style>
:root{
  --orange:#e85613;
  --orange-bright:#ff5e14;
  --navy:#00235a;
  --light:#eceef3;
  --board:#e5e5e5;
  --ink:#1d2a44;
  --muted:#6b7385;
  --white:#fff;
}
*{box-sizing:border-box;margin:0;padding:0}
html,body{width:1200px;height:3127px;overflow:hidden}
body{background:var(--board);font-family:"Barlow",sans-serif;color:var(--ink);position:relative}
.abs{position:absolute}

/* style guide strip */
.brand{display:flex;align-items:center;gap:8px;font-weight:500;color:var(--navy)}
.brand .mark{width:10px;height:10px;background:var(--orange)}
.guide-brand{left:204px;top:142px;font-size:14px}
.guide-title{font-size:26px;font-weight:400;color:var(--navy)}
.guide-font{left:567px;top:143px;font-size:17px;color:#707786}
.swatch{width:41px;height:41px;border-radius:50%;top:138px}
.swatch-label{top:187px;font-size:10px;color:#555;width:50px;text-align:center}

/* site */
.site{left:222px;top:279px;width:790px;height:2745px;background:var(--white);overflow:hidden}
.bg-shapes{position:absolute;left:0;top:0}
.header{left:0;top:0;width:790px;height:33px;background:var(--white)}
.header .brand{position:absolute;left:87px;top:11px;font-size:9px}
.header .brand .mark{width:8px;height:8px}
.nav{position:absolute;top:12px;font-size:8.5px;color:var(--ink)}
.call{position:absolute;display:flex;align-items:center;gap:7px;color:var(--white)}
.call .ico{width:17px;height:17px;border-radius:50%;background:var(--orange-bright);display:flex;align-items:center;justify-content:center}
.call small{display:block;font-size:6.5px;opacity:.8}
.call b{display:block;font-size:8px;font-weight:600}
.header .call{left:571px;top:0;width:105px;height:33px;background:var(--navy);padding-left:14px}

.hero-photo{left:0;top:33px;width:790px;height:386px;clip-path:polygon(0 0,100% 0,100% 100%,0 81%);
  background:linear-gradient(100deg,#8a6a44 0%,#b28f63 30%,#c5a77c 45%,#8f9aa0 62%,#7d6a50 80%,#a58660 100%)}
.hero-title{left:97px;top:134px;font-size:29px;line-height:32px;font-weight:600;color:var(--white);width:380px}
.btn{background:var(--orange-bright);color:var(--white);font-size:8px;font-weight:600;display:flex;align-items:center;justify-content:center}
.hero-btn{left:89px;top:243px;width:103px;height:30px}

.sec-title{font-size:22px;line-height:24px;font-weight:500;color:var(--navy);padding-left:10px;border-left:2px solid var(--orange)}
.sec-title.on-dark{color:var(--white)}
.body-text{font-size:8.5px;line-height:13px;color:var(--muted)}
.photo{background:linear-gradient(160deg,#d6dade,#b9bfc6 55%,#e07445 56%,#c7cdd3 70%)}
.checks{left:631px;top:489px;list-style:none}
.checks li{display:flex;align-items:center;gap:6px;font-size:8px;color:var(--ink);height:27.6px}
.checks li span{width:10px;height:10px;border-radius:50%;background:#fde3d6;display:flex;align-items:center;justify-content:center}

.card{width:193px;height:206px;background:var(--white);top:834px}
.card-photo{position:absolute;left:14px;top:48px;width:165px;height:100px;background:linear-gradient(180deg,#f3f4f6,#c7cbd0 60%,#f3f4f6)}
.card-caption{top:1062px;width:193px;height:29px;display:flex;align-items:center;justify-content:space-between;font-size:10px;color:var(--ink);font-weight:500}
.card-caption.active{border-bottom:1px solid var(--navy)}
.sq{width:29px;height:29px;background:var(--orange-bright);display:flex;align-items:center;justify-content:center}
.sq.navy{background:var(--navy)}

.finest-photo{left:87px;top:1246px;width:282px;height:380px;background:linear-gradient(165deg,#9aa3ab,#c9ccd0 40%,#e06a37 50%,#8e9296 75%,#6f7479)}
.dark-text{color:#c9d1e2;font-size:8px;line-height:14px}
.dark-sub{color:var(--white);font-size:15px;line-height:19px;font-weight:500}
.play{left:436px;top:1447px;width:45px;height:45px;border-radius:50%;background:var(--orange-bright);display:flex;align-items:center;justify-content:center}
.play-label{left:488px;top:1464px;font-size:8px;color:var(--white);font-weight:500}

.quote-card{top:1753px;width:182px;height:182px;border:1px solid #dfe2e8;background:var(--white)}
.quote-card p{position:absolute;left:21px;top:36px;width:145px;font-size:8px;line-height:13.5px;font-style:italic;color:var(--muted)}
.quote-badge{position:absolute;right:0;top:0;width:28px;height:28px;background:var(--orange-bright);color:var(--white);font-size:22px;font-weight:600;text-align:center;line-height:34px}
.quote-name{top:1948px;font-size:8.5px;color:var(--navy);line-height:13px}
.quote-name small{display:block;font-size:7.5px;color:var(--muted)}

.news-photo{left:90px;top:2138px;width:283px;height:119px;background:linear-gradient(120deg,#c9c4bd,#b8aea2 40%,#e8742f 55%,#d8a282 75%,#d2cdc7)}
.news-date{font-size:6.5px;color:var(--muted)}
.news-head{font-size:12.5px;line-height:14px;color:var(--navy)}
.read{font-size:7px;color:var(--orange-bright);font-weight:600}
.news-thumb{left:387px;top:2138px;width:83px;height:56px;background:linear-gradient(180deg,#d9dde2,#8d969f 60%,#b9bec3)}
.divider{height:1px;background:#d8dce4;width:313px;left:390px}

.foot-head{font-size:9px;color:var(--white);font-weight:500}
.foot-head::after{content:"";display:block;width:20px;height:1px;background:var(--orange-bright);margin-top:5px}
.foot-links{font-size:7.5px;line-height:14.5px;color:#b7c1d6}
.foot-call{left:88px;top:2554px;width:105px;height:33px;border:1px solid #fff;padding-left:12px}
.social{display:flex;gap:5px}
.social span{width:7px;height:7px;border-radius:50%;background:var(--white)}
</style>
</head>
<body>

<!-- style guide -->
<div class="abs brand guide-brand"><span class="mark"></span>Marrowbeck Trailers</div>
<div class="abs guide-title" style="left:567px;top:100px">Fonts:</div>
<div class="abs guide-font">Barlow</div>
<div class="abs guide-title" style="left:837px;top:100px">Colors:</div>
<div class="abs swatch" style="left:839px;background:var(--orange)"></div>
<div class="abs swatch" style="left:890px;background:var(--orange-bright)"></div>
<div class="abs swatch" style="left:941px;background:var(--navy)"></div>
<div class="abs swatch" style="left:993px;background:var(--light)"></div>
<div class="abs swatch-label" style="left:834px">#e85613</div>
<div class="abs swatch-label" style="left:885px">#ff5e14</div>
<div class="abs swatch-label" style="left:936px">#00235a</div>
<div class="abs swatch-label" style="left:988px">#ece9e6</div>

<main class="abs site">
  <svg class="bg-shapes" width="790" height="2745" viewBox="0 0 790 2745" aria-hidden="true">
    <polygon points="0,692 790,758 790,1250 0,1250" fill="#eceef3"/>
    <polygon points="0,1132 790,1199 790,1574 0,1507" fill="#00235a"/>
    <polygon points="0,1994 790,2063 790,2470 0,2470" fill="#eceef3"/>
    <polygon points="0,2402 790,2469 790,2745 0,2745" fill="#00235a"/>
    <polygon points="91,2400 790,2457 790,2465 91,2405" fill="#ff5e14"/>
  </svg>

  <header class="abs header">
    <div class="brand"><span class="mark"></span>Marrowbeck Trailers</div>
    <span class="nav" style="left:436px">Home</span>
    <span class="nav" style="left:475px">Trailer Types</span>
    <span class="nav" style="left:537px">News</span>
    <div class="call">
      <span class="ico"><svg width="8" height="8" viewBox="0 0 10 10"><path d="M2 1l2 2-1 1.3c.6 1.2 1.5 2.1 2.7 2.7L7 6l2 2-1.3 1.3C4.7 9 1 5.3.7 2.3z" fill="#fff"/></svg></span>
      <span><small>Call Us Today</small><b>+61 8 5550 1742</b></span>
    </div>
    <svg class="abs" style="left:690px;top:12px" width="10" height="10" viewBox="0 0 10 10"><circle cx="4" cy="4" r="3" fill="none" stroke="#ff5e14" stroke-width="1.2"/><line x1="6.3" y1="6.3" x2="9" y2="9" stroke="#ff5e14" stroke-width="1.2"/></svg>
  </header>

  <section>
    <div class="abs hero-photo" role="img" aria-label="Photo of a galvanised tipper trailer dumping rocks at a quarry, a worker in hi-vis beside it"></div>
    <svg class="abs" style="left:0;top:0" width="790" height="430" aria-hidden="true"><polygon points="0,344 706,410 700,419 0,353" fill="#ff5e14"/></svg>
    <h1 class="abs hero-title">Your Go-To Source for Marrowbeck &amp; Dunmere Ashby Trailers and Floats</h1>
    <div class="abs btn hero-btn">Explore Trailer Types</div>
  </section>

  <section>
    <h2 class="abs sec-title" style="left:87px;top:489px">Quality Trails &amp;<br>Floats for Sale</h2>
    <p class="abs body-text" style="left:97px;top:563px;width:160px">Crafted in the heart of Wales, UK, these trailers are a testament to precision engineering and durability. Designed to endure the harshest conditions of the unforgiving outback, they stand as a symbol of unwavering strength.</p>
    <div class="abs photo" style="left:364px;top:453px;width:154px;height:206px" role="img" aria-label="Photo of an orange mini excavator loaded on a plant trailer"></div>
    <ul class="abs checks">
      <li><span><svg width="6" height="6" viewBox="0 0 6 6"><path d="M1 3l1.3 1.3L5 1.5" stroke="#ff5e14" fill="none"/></svg></span>Text filler only</li>
      <li><span><svg width="6" height="6" viewBox="0 0 6 6"><path d="M1 3l1.3 1.3L5 1.5" stroke="#ff5e14" fill="none"/></svg></span>Text filler only</li>
      <li><span><svg width="6" height="6" viewBox="0 0 6 6"><path d="M1 3l1.3 1.3L5 1.5" stroke="#ff5e14" fill="none"/></svg></span>Text filler only</li>
      <li><span><svg width="6" height="6" viewBox="0 0 6 6"><path d="M1 3l1.3 1.3L5 1.5" stroke="#ff5e14" fill="none"/></svg></span>Text filler only</li>
      <li><span><svg width="6" height="6" viewBox="0 0 6 6"><path d="M1 3l1.3 1.3L5 1.5" stroke="#ff5e14" fill="none"/></svg></span>Text filler only</li>
      <li><span><svg width="6" height="6" viewBox="0 0 6 6"><path d="M1 3l1.3 1.3L5 1.5" stroke="#ff5e14" fill="none"/></svg></span>Text filler only</li>
    </ul>
  </section>

  <section>
    <h2 class="abs sec-title" style="left:87px;top:756px">Highlighted<br>Trailer Types</h2>
    <div class="abs card" style="left:87px"><div class="card-photo" role="img" aria-label="Photo of a galvanised twin-axle general duty trailer with ladder rack"></div></div>
    <div class="abs card" style="left:300px"><div class="card-photo" role="img" aria-label="Photo of a flat-deck tipper trailer"></div></div>
    <div class="abs card" style="left:513px"><div class="card-photo" role="img" aria-label="Photo of a silver horse float with ramp lowered"></div></div>
    <div class="abs card-caption" style="left:87px">RV3072 /RV81 Trailers<span class="sq"><svg width="10" height="10" viewBox="0 0 10 10"><path d="M1 5h8M5.5 1.5L9 5 5.5 8.5" stroke="#fff" fill="none" stroke-width="1.2"/></svg></span></div>
    <div class="abs card-caption active" style="left:300px">LP5840/5296 Tipper Trailers<span class="sq navy"><svg width="10" height="10" viewBox="0 0 10 10"><path d="M1 5h8M5.5 1.5L9 5 5.5 8.5" stroke="#fff" fill="none" stroke-width="1.2"/></svg></span></div>
    <div class="abs card-caption" style="left:513px">QX408/QX412 Horse Floats<span class="sq"><svg width="10" height="10" viewBox="0 0 10 10"><path d="M1 5h8M5.5 1.5L9 5 5.5 8.5" stroke="#fff" fill="none" stroke-width="1.2"/></svg></span></div>
  </section>

  <section>
    <div class="abs finest-photo" role="img" aria-label="Photo of an orange mini excavator on a galvanised plant trailer"></div>
    <h2 class="abs sec-title on-dark" style="left:436px;top:1254px;font-size:21px">The Finest Trailers in Perth:<br>Uncompromising Quality</h2>
    <p class="abs dark-text" style="left:436px;top:1311px;width:300px">At the heart of quality trailers: our commitment to design, engineering, and customer-centric solutions. We take the time to understand your needs and deliver trailers that exceed expectations.</p>
    <p class="abs dark-sub" style="left:436px;top:1364px;width:300px">We pride ourselves on well-designed and engineered trailers.</p>
    <p class="abs dark-text" style="left:436px;top:1409px;width:300px">We pride ourselves on supplying well designed and engineered trailers. Our team take the time to listen to our customers and supply</p>
    <div class="abs play"><svg width="12" height="12" viewBox="0 0 12 12"><path d="M3 2l7 4-7 4z" fill="#fff"/></svg></div>
    <span class="abs play-label">See How it Works</span>
  </section>

  <section>
    <h2 class="abs sec-title" style="left:87px;top:1674px">What Our Clients<br>Say About Us</h2>
    <svg class="abs" style="left:670px;top:1713px" width="32" height="10" viewBox="0 0 32 10"><path d="M11 5H1M4.5 1.5L1 5l3.5 3.5" stroke="#9aa3b5" fill="none"/><path d="M19 5h10M25.5 1.5L29 5l-3.5 3.5" stroke="#00235a" fill="none" stroke-width="1.3"/></svg>

    <div class="abs quote-card" style="left:87px"><span class="quote-badge">&ldquo;</span><p>"I can't express my gratitude enough for the exceptional 3.5-tonne tipping trailer you provided. I really visited numerous places, seeking quotes and ideas for a versatile trailer that could meet all our landscaping business needs"</p></div>
    <div class="abs quote-card" style="left:285px"><span class="quote-badge">&ldquo;</span><p>"From the moment we integrated your trailers into our operations, we've been consistently thrilled with their top-notch quality and outstanding performance."</p></div>
    <div class="abs quote-card" style="left:483px"><span class="quote-badge">&ldquo;</span><p>"An enormous shoutout to the exceptional crew. Your durable and incredibly versatile trailers have been the unwavering backbone of our construction projects. They haven't only but exceeded our expectations, making our work more efficient and reliable day in and day out."</p></div>
    <div class="abs quote-card" style="left:681px"><span class="quote-badge">&ldquo;</span><p>"From the moment we integrated your trailers into our operations, we've been consistently thrilled with their top-notch quality and outstanding performance."</p></div>

    <div class="abs quote-name" style="left:108px">Owen Tallis<small>-Satisfied Customer</small></div>
    <div class="abs quote-name" style="left:306px">Bram Kettering<small>-Satisfied Customer</small></div>
    <div class="abs quote-name" style="left:504px">Silas Hewitt<small>-Satisfied Customer</small></div>
    <div class="abs quote-name" style="left:702px">Dean Morrow<small>-Satisfied Customer</small></div>
  </section>

  <section>
    <h2 class="abs sec-title" style="left:90px;top:2066px">From the News<br>- Blog Posts</h2>
    <div class="abs news-photo" role="img" aria-label="Photo of a worker in a hard hat and hi-vis vest on a phone call"></div>
    <span class="abs news-date" style="left:90px;top:2288px">10/20/2023</span>
    <h3 class="abs news-head" style="left:90px;top:2302px;width:283px;font-weight:400">Trailer workers: Navigating the challenges of long-haul trucking</h3>
    <span class="abs read" style="left:90px;top:2347px">Read Article ›</span>

    <div class="abs news-thumb" role="img" aria-label="Photo of a trailer parked outside a depot"></div>
    <span class="abs news-date" style="left:479px;top:2137px">10/20/2023</span>
    <h3 class="abs news-head" style="left:479px;top:2151px;width:225px;font-weight:400">How a trailer firm's mobile command center is paving the way for global partnerships and much more</h3>
    <div class="abs divider" style="top:2210px"></div>
    <span class="abs news-date" style="left:390px;top:2226px">10/20/2023</span>
    <h3 class="abs news-head" style="left:390px;top:2241px;width:315px;font-weight:400">How trailers are shaping international collaborations and redefining the way global partnerships operate in a dynamic world</h3>
    <div class="abs divider" style="top:2299px"></div>
    <span class="abs news-date" style="left:390px;top:2315px">10/20/2023</span>
    <h3 class="abs news-head" style="left:390px;top:2328px;width:290px;font-weight:400">Unlocking the power of tipper trailers: Hauling and dumping made easy</h3>
  </section>

  <footer>
    <div class="abs brand" style="left:87px;top:2515px;font-size:9px;color:#fff"><span class="mark" style="width:8px;height:8px"></span>Marrowbeck Trailers</div>
    <div class="abs call foot-call">
      <span class="ico"><svg width="8" height="8" viewBox="0 0 10 10"><path d="M2 1l2 2-1 1.3c.6 1.2 1.5 2.1 2.7 2.7L7 6l2 2-1.3 1.3C4.7 9 1 5.3.7 2.3z" fill="#fff"/></svg></span>
      <span><small>Call Us Today</small><b>+61 8 5550 1742</b></span>
    </div>
    <span class="abs foot-links" style="left:87px;top:2665px">© 2023 - All Rights Reserved</span>

    <div class="abs foot-head" style="left:468px;top:2511px">Quick Links</div>
    <div class="abs foot-links" style="left:468px;top:2548px">Trailer Types<br>News<br>Contact<br>Privacy Policy</div>
    <div class="abs foot-head" style="left:468px;top:2628px">Partners</div>
    <div class="abs" style="left:470px;top:2663px;width:38px;height:31px;background:#2f5ea8" role="img" aria-label="Partner badge"></div>
    <div class="abs" style="left:530px;top:2665px;width:158px;height:22px;background:var(--orange)" role="img" aria-label="Partner badge"></div>

    <div class="abs foot-head" style="left:592px;top:2511px">Get in Touch With Us</div>
    <div class="abs foot-links" style="left:592px;top:2548px">+61 8 5550 1742<br><span style="display:block;line-height:11px;margin:2px 0 3px">Street, Address, Number,<br>Avenue, Goes Here</span>info@marrowbeckfloats.com</div>
    <div class="abs social" style="left:592px;top:2616px"><span></span><span></span><span></span></div>
  </footer>
</main>

</body>
</html>
```